Service company standing banner design

We are an existing company that just updated our logo. We are attending some oportunity summits in the near future and want a new crisp clean look on our three banners that will be placed in the back of our small booth. The summits we are attending are designed to give local companies opportunities on a prokect we have been awarded to construct in their area. These banners should communicate who we are with no questions when people see them. One banner shall list our services. One to list our values and one to state our goals. All these while being appealing to the eye and using picture of nature. Attached are copies of what we are to replace. also the new logo and the original background pictures in the existing banners

```html
<!DOCTYPE html>
<html lang="en">
<head>
<meta charset="utf-8">
<title>Tarrow Services – Our Services Banner</title>
<link href="https://fonts.googleapis.com/css2?family=Righteous&display=swap" rel="stylesheet">
<style>
  :root {
    --paper: #ffffff;
    --brand-blue: #1b49a6;
    --brand-orange: #f08a1c;
    --mist-grey: #6f7c79;
    --mist-mauve: #85586a;
    --forest-wine: #8c2b4a;
    --forest-crimson: #a31c3d;
    --text-light: #ffffff;
  }
  * { margin: 0; padding: 0; box-sizing: border-box; }
  html, body {
    width: 1200px;
    height: 2400px;
    overflow: hidden;
    background: var(--paper);
  }
  .banner {
    position: relative;
    width: 1200px;
    height: 2400px;
    overflow: hidden;
    font-family: "Righteous", "Trebuchet MS", sans-serif;
  }
  .forest-backdrop {
    position: absolute;
    inset: 0;
    background:
      radial-gradient(ellipse 70% 30% at 85% 18%, rgba(120,138,132,0.75), rgba(120,138,132,0) 70%),
      radial-gradient(ellipse 60% 25% at 20% 30%, rgba(90,70,84,0.45), rgba(90,70,84,0) 70%),
      linear-gradient(180deg,
        var(--mist-grey) 8%,
        var(--mist-mauve) 35%,
        var(--forest-wine) 62%,
        var(--forest-crimson) 100%);
  }
  .header-edge {
    position: absolute;
    top: 0;
    left: 0;
    width: 1200px;
    height: 420px;
  }
  .brand {
    position: absolute;
    top: 70px;
    left: 80px;
    display: flex;
    align-items: center;
    gap: 36px;
    color: var(--brand-blue);
  }
  .brand-dot {
    width: 190px;
    height: 190px;
    border-radius: 50%;
    background: var(--brand-orange);
    flex: none;
  }
  .brand-name {
    line-height: 1;
    color: var(--brand-blue);
  }
  .brand-name .line-main {
    display: block;
    font-size: 104px;
    letter-spacing: 0.005em;
  }
  .brand-name .line-sub {
    display: block;
    font-size: 70px;
    margin-top: 22px;
    letter-spacing: 0.03em;
  }
  .service-list {
    position: absolute;
    top: 640px;
    left: 100px;
    list-style: none;
  }
  .service-item {
    display: flex;
    align-items: center;
    height: 213px;
    color: var(--text-light);
    font-size: 78px;
    letter-spacing: 0.12em;
    margin-top: -106px;
    margin-bottom: 106px;
  }
  .service-item::before {
    content: "";
    width: 34px;
    height: 34px;
    border-radius: 50%;
    background: var(--text-light);
    margin-right: 32px;
    margin-top: 18px;
    flex: none;
  }
</style>
</head>
<body>
  <main class="banner">
    <div class="forest-backdrop" role="img" aria-label="Misty evergreen forest photograph fading from grey mist into deep crimson"></div>

    <svg class="header-edge" viewBox="0 0 1200 420" aria-hidden="true">
      <path fill="var(--paper)" d="M0 0 H1200 V285 L1170 292 L1130 300 L1095 312 L1060 306 L1020 318 L985 312 L950 320 L910 314 L880 326 L850 318 L815 330 L780 322 L745 336 L705 330 L670 342 L635 334 L600 348 L560 344 L525 356 L490 350 L455 360 L420 352 L385 366 L350 360 L315 372 L280 364 L245 378 L210 370 L175 382 L140 376 L105 388 L70 380 L35 392 L0 386 Z"/>
    </svg>

    <header class="brand">
      <span class="brand-dot" aria-hidden="true"></span>
      <h1 class="brand-name">
        <span class="line-main">Tarrow Services</span>
        <span class="line-sub">Limited Partnership</span>
      </h1>
    </header>

    <ul class="service-list">
      <li class="service-item">Logging</li>
      <li class="service-item">Mulching</li>
      <li class="service-item">Civil Works</li>
      <li class="service-item">Reclamation</li>
      <li class="service-item">Land Clearing</li>
      <li class="service-item">Pipeline Clearing</li>
      <li class="service-item">Road maintenance</li>
      <li class="service-item">Pipeline Construcrion</li>
    </ul>
  </main>
</body>
</html>
```